Zielgruppe
Beratung und Live-Kommunikation
Aufgabenstellung
- Re-Design vom Firmenlogo und Briefpapier
- Anpassung/ Abwandlung der vorhandenen Elemente (Briefkopf). Anordnung, Schrift, etc.
- Ideen, wie man den Inhalt (den Tätigkeitsbereich) ggfs. grafisch ansprechend als Logo darstellen kann.
- Klare Linien, symmetrisch. Schwarz-weiß/keine Farbe
- Briefpapier auf *.doc Basis, kein randloser Druck
- derzeitiger Stil siehe www.buehnenwerkraum.de

```html
<!DOCTYPE html>
<html lang="de">
<head>
<meta charset="utf-8">
<title>Briefpapier – wertheim bühnenbüro</title>
<link rel="stylesheet" href="https://fonts.googleapis.com/css2?family=Didact+Gothic&display=swap">
<style>
  :root {
    --paper: #ffffff;
    --ink: #111111;
    --ink-soft: #333333;
    --mark: #9a9a9a;
  }
  html, body { margin: 0; padding: 0; overflow: hidden; }
  body { width: 858px; height: 1200px; background: var(--paper); }
  .letterhead {
    position: relative; width: 858px; height: 1200px;
    background: var(--paper); color: var(--ink);
    font-family: "Didact Gothic", "Century Gothic", sans-serif;
  }
  .brand { position: absolute; left: 560px; top: 104px; width: 259px; text-align: right; }
  .brand-name { font-size: 24px; line-height: 26px; letter-spacing: 0.2px; }
  .brand-sub { font-size: 11.5px; line-height: 12px; letter-spacing: 1.2px; }

  .services { position: absolute; left: 596px; top: 162px; list-style: none; margin: 0; padding: 0; }
  .services li { display: flex; align-items: center; height: 24px; font-size: 20px; }
  .services svg { width: 20px; height: 20px; margin-right: 7px; }

  .window-mark { position: absolute; width: 9px; height: 9px; border-color: var(--mark); border-style: solid; border-width: 0; }
  .tl { left: 97px; top: 181px; border-top-width: 1px; border-left-width: 1px; }
  .tr { left: 435px; top: 181px; border-top-width: 1px; border-right-width: 1px; }
  .bl { left: 97px; top: 354px; border-bottom-width: 1px; border-left-width: 1px; }
  .br { left: 435px; top: 354px; border-bottom-width: 1px; border-right-width: 1px; }
  .sender-line { position: absolute; left: 117px; top: 188px; font-size: 12px; }

  .fold-mark { position: absolute; left: 13px; width: 11px; height: 0; border-top: 1px solid var(--mark); }
  .fold-1 { top: 424px; } .fold-2 { top: 847px; }

  .contact { position: absolute; left: 596px; top: 836px; font-size: 11.5px; line-height: 14px; color: var(--ink-soft); }
  .contact .row { display: flex; align-items: flex-start; margin-bottom: 8px; }
  .contact .row.gap { margin-bottom: 26px; }
  .contact svg { width: 17px; height: 17px; flex: none; margin-right: 9px; }
  .contact strong { color: var(--ink); font-weight: 700; }
  .contact .spacer { height: 14px; }

  .payment-note {
    position: absolute; left: 97px; top: 1076px; width: 462px;
    font-size: 11.3px; line-height: 14px; color: var(--ink-soft); margin: 0;
  }
</style>
</head>
<body>
<div class="letterhead">

  <header class="brand">
    <div class="brand-name">jonas wertheim</div>
    <div class="brand-sub">bühnenbüro</div>
  </header>

  <ul class="services">
    <li><svg viewBox="0 0 20 20"><rect width="20" height="20" rx="3" fill="#111"/><path d="M4 5h12v8H9l-3 3v-3H4z" fill="none" stroke="#fff" stroke-width="1.4"/></svg>beratung</li>
    <li><svg viewBox="0 0 20 20"><rect width="20" height="20" rx="3" fill="#111"/><circle cx="10" cy="8" r="4" fill="none" stroke="#fff" stroke-width="1.4"/><path d="M8 13h4M8 15.5h4" stroke="#fff" stroke-width="1.4"/></svg>planung</li>
    <li><svg viewBox="0 0 20 20"><rect width="20" height="20" rx="3" fill="#111"/><circle cx="10" cy="10" r="5.5" fill="none" stroke="#fff" stroke-width="2" stroke-dasharray="2.2 1.4"/><circle cx="10" cy="10" r="2" fill="#fff"/></svg>umsetzung</li>
  </ul>

  <span class="window-mark tl"></span><span class="window-mark tr"></span>
  <span class="window-mark bl"></span><span class="window-mark br"></span>
  <div class="sender-line">Wertheim &nbsp;|&nbsp; Lindenweg 4b &nbsp;|&nbsp; D-50999 Musterstadt</div>

  <span class="fold-mark fold-1"></span>
  <span class="fold-mark fold-2"></span>

  <footer class="contact">
    <div class="row gap-s"><svg viewBox="0 0 20 20"><rect width="20" height="20" rx="3" fill="#111"/><path d="M10 16s-4-4.5-4-7.5a4 4 0 0 1 8 0c0 3-4 7.5-4 7.5z" fill="none" stroke="#fff" stroke-width="1.4"/></svg>
      <div><strong>wertheim bühnenbüro GmbH</strong><br>Lindenweg 4b<br>D-50999 Musterstadt</div></div>
    <div class="row"><svg viewBox="0 0 20 20"><rect width="20" height="20" rx="3" fill="#111"/><circle cx="10" cy="10" r="5.5" fill="none" stroke="#fff" stroke-width="1"/><path d="M4.5 10h11M10 4.5c-3 3-3 8 0 11M10 4.5c3 3 3 8 0 11" fill="none" stroke="#fff" stroke-width="1"/></svg><div>buehnenbuero.gmbh</div></div>
    <div class="row"><svg viewBox="0 0 20 20"><rect width="20" height="20" rx="3" fill="#111"/><path d="M6 4.5l2.5 2.5-1.5 2c1 2 2 3 4 4l2-1.5 2.5 2.5-2 2c-5 0-9.5-4.5-9.5-9.5z" fill="#fff"/></svg><div>+49 (0)170 123 456 78</div></div>
    <div class="row"><svg viewBox="0 0 20 20"><rect width="20" height="20" rx="3" fill="#111"/><rect x="4.5" y="6" width="11" height="8" fill="none" stroke="#fff" stroke-width="1"/><path d="M4.5 6l5.5 4.5L15.5 6" fill="none" stroke="#fff" stroke-width="1"/></svg><div>wertheim@buehnenbuero.gmbh</div></div>
    <div class="row gap"><svg viewBox="0 0 20 20"><rect width="20" height="20" rx="3" fill="#111"/><rect x="6" y="6" width="8" height="8" fill="none" stroke="#fff" stroke-width="1.4"/></svg><div>wertheim_live</div></div>
    <div class="row gap"><svg viewBox="0 0 20 20"><rect width="20" height="20" rx="3" fill="#111"/><path d="M4.5 8L10 5l5.5 3zM5 15h10M6.5 9v5M10 9v5M13.5 9v5" fill="none" stroke="#fff" stroke-width="1.2"/></svg>
      <div>Musterbank Rheinland<br>IBAN de00.1234.5678.9012.3456.78<br>BIC MUSTDEXXXXX</div></div>
    <div class="row"><svg viewBox="0 0 20 20"><rect width="20" height="20" rx="3" fill="#111"/><rect x="5" y="4" width="9" height="12" fill="none" stroke="#fff" stroke-width="1.2"/><path d="M7 7h5M7 9.5h5M7 12h3" stroke="#fff" stroke-width="1"/></svg>
      <div>Jonas Wertheim<br>Finanzamt Musterstadt<br>Steuer-Nr. 000.1111.2222<br>USt-IdNr. DE000.111.222<div class="spacer"></div>Amtsgericht Musterstadt HRB 00000</div></div>
  </footer>

  <p class="payment-note">Endbetrag zahlbar sofort nach Erhalt innerhalb von 10 Tagen ohne Abzug auf das genannte Konto. Die Leistung ist bereits erbracht. Der Betrag wird beim Finanzamt Musterstadt ordnungsgemäß versteuert. Eine erweiterte Aufschlüsselung der Summen und Belegkopien befinden sich ggfs. in der Anlage. Auslagen und Verpflegungsmehraufwendungen können separat in Rechnung gestellt werden.</p>

</div>
</body>
</html>
```